TRU PEAK POWER.

I'd like my business logo.
contact name: Desmond Halvik
phone:0438275160
email: info@trupeakpower.net.au
website: www.trupeakpower.net.au

services:
solar
battery storage
LED lighting
energy saving solutions
general electrical
I'd like the design to look professional

Target Market(s)

Everyone

Industry/Entity Type

Business

Contact Information for Business Card

as described above

Requirements
Must have
• Id like the colours and the design to work well with my logo.

```html
<!DOCTYPE html>
<html lang="en">
<head>
<meta charset="utf-8">
<title>Tru Peak Power – Business Card</title>
<link rel="stylesheet" href="https://fonts.googleapis.com/css2?family=Open+Sans:wght@400;600;700&display=swap">
<style>
  :root {
    --page-bg: #e9e6df;
    --card-white: #ffffff;
    --green-deep: #2f9a35;
    --green-mid: #4cae32;
    --green-light: #8cc63f;
    --sun-orange: #f3a521;
    --swoosh-grey: #dfe2dc;
    --text-green: #3b9a34;
    --text-white: #ffffff;
  }
  html, body {
    margin: 0;
    width: 1200px;
    height: 843px;
    overflow: hidden;
    background: var(--page-bg);
    font-family: "Open Sans", Arial, sans-serif;
  }
  .canvas {
    position: relative;
    width: 1200px;
    height: 843px;
  }
  .business-card {
    position: absolute;
    left: 150px;
    top: 164px;
    width: 900px;
    height: 515px;
    background: var(--card-white);
    border-radius: 26px;
    overflow: hidden;
    box-shadow: 0 12px 34px rgba(0,0,0,0.18);
  }
  .card-swoosh {
    position: absolute;
    inset: 0;
    width: 900px;
    height: 515px;
  }
  .brand {
    position: absolute;
    left: 56px;
    top: 130px;
    display: flex;
    align-items: center;
    gap: 14px;
  }
  .brand-dot {
    width: 40px;
    height: 40px;
    border-radius: 50%;
    background: var(--green-mid);
  }
  .brand-name {
    font-weight: 700;
    font-size: 32px;
    letter-spacing: 0.5px;
    color: var(--text-green);
  }
  .contact-name {
    position: absolute;
    left: 58px;
    top: 232px;
    margin: 0;
    font-weight: 700;
    font-size: 28px;
    color: var(--text-green);
  }
  .contact-list, .service-list {
    position: absolute;
    left: 600px;
    margin: 0;
    padding: 0;
    list-style: none;
    color: var(--text-white);
  }
  .contact-list { top: 110px; font-size: 17px; line-height: 34px; }
  .service-list { top: 262px; font-size: 21px; font-weight: 600; line-height: 38px; }
  .contact-list li, .service-list li {
    display: flex;
    align-items: center;
    gap: 12px;
  }
  .icon { width: 16px; height: 16px; flex: none; }
  .service-list .icon { width: 18px; height: 18px; }
</style>
</head>
<body>
<main class="canvas">
  <article class="business-card">
    <svg class="card-swoosh" viewBox="0 0 900 515" aria-hidden="true">
      <defs>
        <linearGradient id="greenFill" x1="0" y1="0" x2="1" y2="1">
          <stop offset="0" stop-color="var(--green-light)"/>
          <stop offset="1" stop-color="var(--green-deep)"/>
        </linearGradient>
      </defs>
      <path d="M380,0 C500,130 390,360 480,515 L900,515 L900,0 Z" fill="var(--swoosh-grey)"/>
      <path d="M392,0 C510,130 402,360 492,515" fill="none" stroke="var(--sun-orange)" stroke-width="3"/>
      <path d="M420,0 C540,130 430,360 520,515 L900,515 L900,0 Z" fill="url(#greenFill)"/>
      <path d="M430,0 C560,110 470,300 545,515 L565,515 C500,310 585,120 470,0 Z" fill="var(--green-light)" opacity="0.55"/>
    </svg>

    <div class="brand">
      <span class="brand-dot"></span>
      <span class="brand-name">TRU PEAK POWER</span>
    </div>

    <h1 class="contact-name">Desmond Halvik</h1>

    <ul class="contact-list">
      <li><svg class="icon" viewBox="0 0 16 16"><path d="M4 1l3 3-2 2c1 2 3 4 5 5l2-2 3 3-2 3C7 15 1 9 1 3z" fill="currentColor"/></svg>0438275160</li>
      <li><svg class="icon" viewBox="0 0 16 16"><rect x="1" y="3" width="14" height="10" rx="1" fill="currentColor"/><path d="M1 4l7 5 7-5" fill="none" stroke="var(--green-mid)" stroke-width="1.5"/></svg>info@trupeakpower.net.au</li>
      <li><svg class="icon" viewBox="0 0 16 16" fill="none" stroke="currentColor" stroke-width="1.4"><circle cx="8" cy="8" r="6.5"/><ellipse cx="8" cy="8" rx="3" ry="6.5"/><path d="M1.5 8h13"/></svg>www.trupeakpower.net.au</li>
    </ul>

    <ul class="service-list">
      <li><svg class="icon" viewBox="0 0 18 18"><path d="M9 0l2 6 6-2-4 5 4 5-6-2-2 6-2-6-6 2 4-5-4-5 6 2z" fill="currentColor"/></svg>Solar</li>
      <li><svg class="icon" viewBox="0 0 18 18"><path d="M9 0l2 6 6-2-4 5 4 5-6-2-2 6-2-6-6 2 4-5-4-5 6 2z" fill="currentColor"/></svg>Battery storage</li>
      <li><svg class="icon" viewBox="0 0 18 18"><path d="M9 0l2 6 6-2-4 5 4 5-6-2-2 6-2-6-6 2 4-5-4-5 6 2z" fill="currentColor"/></svg>LED lighting</li>
      <li><svg class="icon" viewBox="0 0 18 18"><path d="M9 0l2 6 6-2-4 5 4 5-6-2-2 6-2-6-6 2 4-5-4-5 6 2z" fill="currentColor"/></svg>Energy saving solutions</li>
    </ul>
  </article>
</main>
</body>
</html>
```